Cake website needs a professional WordPress design makeover!

I need a wordpress design for my company called Velvet Crumbhouse. It's a home cake business and I specialise in everything from cupcakes, celebratory cakes to couture wedding cakes. I have an existing one page wordpress website www.velvetcrumbhouse.com but it doesn't quite communicate elegance or showcase my skills so it desperately needs a complete change.

I purchased this theme
http://tilecraftery.com/demos/themes/?product=lumo
I basically want my website to look EXACTLY like this. I would obviously provide pictures of my work. I like the positioning of the pictures and texts and how each section are divided with the pictures. I also like the pop up of the welcome text on the home page. I would like that to say Welcome Velvet Crumbhouse.

One element I would like to keep from my original website are the slides on the home page. But will have a different caption with each slide. I will provide the three pictures for these slides.

The page format should be as follows:

Home
Discover Our Story
Tasteful Delights (Picture)
Discover Our Cakes - Clickable link below description going to the full cake menu with prices
The Perfect Blend (Picture)
Our Promise
Discover Your Special Day (Picture)
Wedding Cakes
Make an Order (Picture)
Get in touch

The menu on top of the page should read
Home, Our story, Our Cakes, Price List, Wedding cakes, Get in Touch

I would like to see the page of the full cake menu with the prices.
Signature colours Black, White and Pink

Target Market(s)

My main audience is targeted at women.

Industry/Entity Type

Wedding

Requirements
Must have
• Must look like the link I provided. Please use this as reference.
Nice to have
• Nice to see aspects of my logo, example the butterflies or the paisley design be subtly used around the website.

```html
<!DOCTYPE html>
<html lang="en">
<head>
<meta charset="utf-8">
<title>Velvet Crumbhouse</title>
<link rel="stylesheet" href="https://fonts.googleapis.com/css2?family=Cabin:wght@400;500&family=Herr+Von+Muellerhoff&family=Source+Sans+3:wght@400;700;900&display=swap">
<style>
:root{
  --ink:#2a2a2a;
  --text:#4a4a4a;
  --accent:#d08a7c;
  --white:#ffffff;
  --paper:#ffffff;
  --footer:#171717;
  --footer-bar:#202020;
  --footer-text:#b9b9b9;
  --field:#f1f1f1;
  --field-text:#9a9a9a;
  --social:#5a5a5a;
}
*{box-sizing:border-box;margin:0;padding:0}
html,body{width:1200px;height:4500px;overflow:hidden}
body{position:relative;background:var(--paper);font-family:"Cabin",sans-serif;color:var(--text)}
.abs{position:absolute}
.photo{position:absolute;display:block}

/* header */
.site-header{position:absolute;left:0;top:0;width:1200px;height:90px;z-index:5}
.brand{position:absolute;left:37px;top:28px;display:flex;align-items:center;gap:10px;color:var(--white);font-size:17px;font-weight:500;letter-spacing:1px}
.brand-square{width:18px;height:18px;background:var(--white)}
.main-nav{position:absolute;left:262px;top:36px;display:flex;gap:50px;font-size:15px;color:var(--white);letter-spacing:.5px;white-space:nowrap}

/* hero */
.hero{position:absolute;left:0;top:0;width:1200px;height:832px;background:linear-gradient(100deg,#f3ece8 0%,#e9d6d2 22%,#e98a7d 45%,#f0796b 65%,#f4a093 100%)}
.hero-title{position:absolute;left:400px;top:345px;width:470px;text-align:center;color:var(--white)}
.script{font-family:"Herr Von Muellerhoff",cursive;font-weight:400;line-height:1}
.hero-title .script{font-size:96px;margin-bottom:-22px}
.hero-title h1{font-family:"Source Sans 3",sans-serif;font-weight:900;font-size:38px;letter-spacing:5px;border-top:1px solid rgba(255,255,255,.8);border-bottom:1px solid rgba(255,255,255,.8);padding:2px 0 4px;display:inline-block;white-space:nowrap}
.hero-btn{display:inline-block;margin-top:18px;border:1px solid var(--white);padding:6px 14px;font-size:11px;letter-spacing:2px}
.hero-chevron{position:absolute;left:570px;top:792px;width:60px;height:40px}
.slider-dots{position:absolute;left:1110px;display:flex;flex-direction:column;gap:10px}
.slider-dots span{width:9px;height:9px;border-radius:50%;border:1.5px solid var(--white)}
.slider-dots span.on{background:var(--white)}

/* headings */
.section-heading{position:absolute;text-align:center}
.section-heading .script{color:var(--accent);font-size:92px;margin-bottom:-30px}
.section-heading h2{font-family:"Source Sans 3",sans-serif;font-weight:900;font-size:42px;letter-spacing:5px;color:var(--ink);white-space:nowrap}
.diamond{width:8px;height:8px;background:var(--accent);transform:rotate(45deg);margin:16px auto 0}
.body-copy{position:absolute;font-size:15px;line-height:1.75;text-align:center;color:var(--text)}
.text-link{position:absolute;font-size:12px;letter-spacing:2px;color:var(--accent);border-bottom:1px solid var(--accent);padding-bottom:3px;white-space:nowrap}

/* photo bands */
.band{position:absolute;left:0;width:1200px}
.band-edge{position:absolute;left:0;width:1200px;height:10px}

/* footer */
.site-footer{position:absolute;left:0;top:3818px;width:1200px;height:682px;background:var(--footer);color:var(--white)}
.footer-heading{font-size:14px;letter-spacing:3px;color:var(--white);white-space:nowrap}
.footer-copy{position:absolute;left:375px;top:138px;width:450px;text-align:center;font-size:15px;line-height:1.75;color:var(--white)}
.social{position:absolute;left:232px;top:362px;display:flex;gap:16px}
.social span{width:18px;height:18px;border-radius:50%;background:var(--social)}
.newsletter-input{position:absolute;left:667px;top:356px;width:225px;height:30px;background:var(--field);font-size:11px;color:var(--field-text);padding:8px 10px}
.to-top{position:absolute;left:582px;top:480px;width:36px;height:36px}
.footer-bar{position:absolute;left:0;top:510px;width:1200px;height:172px;background:var(--footer-bar);text-align:center;font-size:12px;color:var(--footer-text);letter-spacing:1px}
.footer-bar .meta{margin-top:48px}
.footer-bar .meta b{color:var(--accent);font-weight:400}
.footer-bar .legal{margin-top:26px;letter-spacing:2px}
</style>
</head>
<body>

<svg width="0" height="0" style="position:absolute">
  <defs>
    <pattern id="zig-down" width="14" height="10" patternUnits="userSpaceOnUse">
      <path d="M0 0 H14 V3 L7 9 L0 3 Z" fill="#ffffff"/>
    </pattern>
    <pattern id="zig-up" width="14" height="10" patternUnits="userSpaceOnUse">
      <path d="M0 10 H14 V7 L7 1 L0 7 Z" fill="#ffffff"/>
    </pattern>
  </defs>
</svg>

<header class="site-header">
  <div class="brand"><span class="brand-square"></span>Velvet Crumbhouse</div>
  <nav class="main-nav">
    <span>Home</span>
    <span>Our Story</span>
    <span>Our Cakes</span>
    <span>Price List</span>
    <span>Wedding Cakes</span>
    <span>Get in Touch</span>
  </nav>
</header>

<section class="hero" id="home" role="img" aria-label="Home slide: close-up of a pink rose-piped cake beside a bowl of strawberries">
  <div class="hero-title">
    <div class="script">Welcome to</div>
    <h1>VELVET CRUMBHOUSE</h1><br>
    <span class="hero-btn">DISCOVER MORE</span>
  </div>
  <div class="slider-dots" style="top:430px"><span class="on"></span><span></span><span></span></div>
  <svg class="hero-chevron" viewBox="0 0 60 40"><path d="M0 40 L30 10 L60 40 Z" fill="#fff"/><path d="M24 20 L30 26 L36 20" fill="none" stroke="#888" stroke-width="2"/></svg>
</section>

<section class="story" id="our-story">
  <div class="section-heading" style="left:150px;top:950px;width:340px">
    <div class="script">Discover</div>
    <h2>OUR STORY</h2>
    <div class="diamond"></div>
  </div>
  <p class="body-copy" style="left:50px;top:1135px;width:540px">Founded in 2012 by a self-taught baker, Marla Ellison created Velvet Crumbhouse as a way to combine her creativity, hard work and passion for baking into perfecting the art of cake baking and decorating. Our mission? It's simple: create a cake that not only looks great but tastes delicious – a cake to be truly proud of.</p>
  <span class="text-link" style="left:282px;top:1298px">ABOUT US</span>
  <div class="photo" style="left:620px;top:911px;width:243px;height:364px;background:linear-gradient(180deg,#5d4a3e,#c8a27e 45%,#3b2c25)" role="img" aria-label="Cupcake with swirled caramel frosting"></div>
  <div class="photo" style="left:911px;top:911px;width:244px;height:364px;background:linear-gradient(160deg,#e9e6e4,#b9b3b0 50%,#6f6866)" role="img" aria-label="Silver cake forks beside a white cake"></div>
</section>

<section class="band" id="tasteful-delights" style="top:1418px;height:540px">
  <div class="photo" style="left:0;top:0;width:382px;height:540px;background:linear-gradient(160deg,#f3e7d2,#d9b889 55%,#8e6a45)" role="img" aria-label="Tasteful Delights: cupcakes with cream frosting and chocolate toppers"></div>
  <div class="photo" style="left:391px;top:0;width:418px;height:540px;background:linear-gradient(180deg,#b7a8a0,#cfdcd3 45%,#e8eeea 80%,#f1d9d6)" role="img" aria-label="Tasteful Delights: mint lace wedding cake with sugar flower"></div>
  <div class="photo" style="left:818px;top:0;width:382px;height:540px;background:linear-gradient(160deg,#6a5a55,#b78c86 45%,#d9a39f 80%,#5a4a44)" role="img" aria-label="Tasteful Delights: novelty cupcakes with pink piped decorations"></div>
  <svg class="band-edge" style="top:0"><rect width="1200" height="10" fill="url(#zig-down)"/></svg>
  <svg class="band-edge" style="top:530px"><rect width="1200" height="10" fill="url(#zig-up)"/></svg>
  <div class="slider-dots" style="top:170px"><span class="on"></span><span></span><span></span><span></span></div>
</section>

<section class="cakes" id="our-cakes">
  <div class="photo" style="left:45px;top:2220px;width:255px;height:182px;background:linear-gradient(150deg,#d8cdbd,#b9a58a 60%,#e8e2d8)" role="img" aria-label="Cupcakes with carrot decorations"></div>
  <div class="photo" style="left:319px;top:2220px;width:262px;height:182px;background:linear-gradient(150deg,#d6a5a3,#c18c88 60%,#eed3d1)" role="img" aria-label="Pink lace celebration cake"></div>
  <div class="photo" style="left:45px;top:2430px;width:255px;height:195px;background:linear-gradient(150deg,#e7e4d2,#c9d1a4 55%,#b8a888)" role="img" aria-label="Cupcakes with green cream frosting"></div>
  <div class="photo" style="left:319px;top:2430px;width:262px;height:195px;background:linear-gradient(150deg,#e2b5b5,#6b4a3c 55%,#c98b8e)" role="img" aria-label="Chocolate-dipped strawberries and pink treats"></div>
  <div class="section-heading" style="left:740px;top:2075px;width:320px">
    <div class="script">Discover</div>
    <h2>CAKES</h2>
    <div class="diamond"></div>
  </div>
  <p class="body-copy" style="left:645px;top:2262px;width:500px;font-size:14.5px">Velvet Crumbhouse offers a wide range of cakes and baked treats using fine, fresh ingredients. We specialise in creating delicious cakes that cater for every event or occasion, from christenings, birthdays and weddings through to themed parties and corporate functions. No matter what size, style or flavour you're after, we make any cake to order, and offer a one-to-one consultation with you to personalise a cake to your needs. And for that personal touch all sugarpaste decorative features are handmade and can be tailored to your requirements and budget. Looking for something more traditional? Why not try our beautiful layered cakes. These cakes are available in a variety of classic flavours as well as some Velvet Crumbhouse specialties. Each cake is comprised of three delicious layers of cake surrounding two layers of our famous light and fluffy buttercream of your choice.</p>
  <span class="text-link" style="left:844px;top:2626px">SEE PRICING</span>
</section>

<section class="band" id="special-day" style="top:2745px;height:540px;background:linear-gradient(180deg,#e8b0a8 0%,#c98c6b 35%,#d9497e 60%,#f2d8c8 100%)" role="img" aria-label="Discover Your Special Day: table of layered cakes, tarts and cupcakes on a pink cloth">
  <svg class="band-edge" style="top:0"><rect width="1200" height="10" fill="url(#zig-down)"/></svg>
  <svg class="band-edge" style="top:530px"><rect width="1200" height="10" fill="url(#zig-up)"/></svg>
  <div class="section-heading" style="left:330px;top:225px;width:540px">
    <div class="script" style="color:#f5e6e2">Discover</div>
    <h2 style="color:#fff">YOUR SPECIAL DAY</h2>
  </div>
  <div class="slider-dots" style="top:175px"><span class="on"></span><span></span><span></span></div>
</section>

<section class="wedding" id="wedding-cakes">
  <p class="body-copy" style="left:60px;top:3492px;width:500px;font-size:14.5px">Discover your special day with a couture wedding cake designed around you. Every tier is baked to order, finished by hand and delivered with care, from intimate gatherings to grand celebrations. Book a tasting to talk through flavours, style and finishing touches.</p>
  <span class="text-link" style="left:287px;top:3634px">MORE</span>
  <div class="photo" style="left:622px;top:3350px;width:248px;height:362px;background:linear-gradient(180deg,#e9e2dc,#e55b6c 35%,#f3b34a 50%,#6cc06c 62%,#5f8fd6 75%,#d9d2cc)" role="img" aria-label="Wedding cakes: slice of rainbow layer cake"></div>
  <div class="photo" style="left:911px;top:3350px;width:244px;height:362px;background:linear-gradient(170deg,#e2d6b8,#f0d37a 40%,#5a4f6b 65%,#eee3c8)" role="img" aria-label="Wedding cakes: tiered stand of yellow and lavender cupcakes"></div>
</section>

<footer class="site-footer" id="get-in-touch">
  <div class="abs footer-heading" style="left:0;width:1200px;top:70px;text-align:center">GET IN TOUCH</div>
  <svg class="abs" style="left:588px;top:102px" width="24" height="14" viewBox="0 0 24 14"><path d="M2 12 Q12 -4 22 12" fill="none" stroke="#fff" stroke-width="1.5"/></svg>
  <p class="footer-copy">Ready to make an order? Tell us about your occasion, your date and the flavours you love, and we will reply within two working days to arrange a friendly consultation and tasting.</p>
  <div class="abs footer-heading" style="left:340px;top:310px;font-size:12px">FOLLOW ALONG</div>
  <div class="social"><span></span><span></span><span></span><span></span></div>
  <div class="abs footer-heading" style="left:705px;top:302px;font-size:12px">NEWSLETTER</div>
  <div class="newsletter-input">Your email address</div>
  <div class="slider-dots" style="top:358px;left:1112px"><span class="on"></span><span></span><span></span><span></span></div>
  <svg class="to-top" viewBox="0 0 36 36"><path d="M0 36 L18 8 L36 36 Z" fill="#202020"/><path d="M13 26 L18 21 L23 26" fill="none" stroke="#fff" stroke-width="2"/></svg>
  <div class="footer-bar">
    <div class="meta">© LUMO 2014 &nbsp;·&nbsp; 14 Linden Row, Bristol &nbsp;·&nbsp; T.01632 960 418 &nbsp;·&nbsp; Handcrafted with love by <b>Tilecraftery Team</b></div>
    <div class="legal">PERMISSIONS AND COPYRIGHT &nbsp;·&nbsp; CONTACT THE TEAM</div>
  </div>
</footer>

</body>
</html>
```